Brenmore Electrical flyer

I need a flyer for my electrical business. All information can be found on the website https://brenmoreelectrical-example.com/. All logos and designs are included in the files to be used.

```html
<!DOCTYPE html>
<html lang="en">
<head>
<meta charset="utf-8">
<title>Brenmore Electrical Flyer</title>
<link href="https://fonts.googleapis.com/css2?family=Montserrat:wght@400;500;600;700&family=Poppins:wght@600&family=Roboto+Condensed:wght@700&display=swap" rel="stylesheet">
<style>
  :root {
    --blue: #0b4fa3;
    --blue-deep: #083b80;
    --orange: #ee8652;
    --orange-strong: #e8612a;
    --yellow: #f7c51c;
    --ink: #2b2b2b;
    --grey: #6a6a6a;
    --page: #ffffff;
    --backdrop: #d6d6d6;
  }
  * { margin: 0; padding: 0; box-sizing: border-box; }
  html, body { width: 1200px; height: 1200px; overflow: hidden; }
  body { background: var(--backdrop); position: relative; font-family: "Montserrat", sans-serif; }

  .flyer {
    position: absolute; left: 218px; top: 60px;
    width: 764px; height: 1080px;
    background: var(--page); overflow: hidden;
  }
  .art { position: absolute; left: 0; top: 0; }

  .brand-mark {
    position: absolute; left: 159px; top: 72px;
    width: 70px; height: 70px; background: var(--orange);
  }
  .brand-name {
    position: absolute; left: 31px; top: 184px; width: 326px;
    text-align: center; white-space: nowrap;
    font-weight: 700; font-size: 23px; line-height: 30px; letter-spacing: -0.3px;
    color: var(--blue);
  }
  .brand-tagline {
    position: absolute; left: 31px; top: 218px; width: 330px;
    text-align: center; white-space: nowrap;
    font-size: 10px; line-height: 12px; letter-spacing: 6px;
    color: var(--grey);
  }

  .intro { position: absolute; left: 31px; top: 262px; width: 326px; }
  .intro p {
    font-size: 11.3px; line-height: 16.8px; color: var(--ink);
    text-align: justify; margin-bottom: 16px;
  }

  .quote-label {
    position: absolute; left: 540px; top: 360px; width: 180px;
    font-family: "Roboto Condensed", sans-serif; font-weight: 700;
    font-size: 37px; line-height: 36px; color: #fff; text-align: center;
  }

  .services-title {
    position: absolute; left: 342px; top: 601px;
    font-weight: 700; font-size: 23px; color: #fff; letter-spacing: 0.3px;
  }
  .service {
    position: absolute; width: 198px; text-align: center;
    font-family: "Poppins", sans-serif; font-weight: 600; font-size: 23px; color: var(--blue);
  }
  .service .bolt { display: inline-block; width: 12px; height: 20px; vertical-align: -1px; margin-right: 2px; }

  .contact-note {
    position: absolute; left: 430px; top: 884px; width: 300px; text-align: center;
    font-weight: 700; font-size: 9px; line-height: 12px; color: var(--ink); text-transform: uppercase;
  }
  .contact-note .lead { color: var(--blue); }
  .phone {
    position: absolute; left: 440px; top: 921px; width: 290px;
    display: flex; align-items: center; justify-content: flex-end; gap: 8px;
    font-weight: 700; font-size: 36px; color: var(--blue); letter-spacing: -1px;
  }
  .website {
    position: absolute; left: 440px; top: 974px; width: 286px; height: 36px;
    background: var(--orange-strong); color: #fff;
    font-weight: 600; font-size: 14.5px; line-height: 36px; text-align: center;
  }
  .email {
    position: absolute; left: 440px; top: 1018px; width: 290px;
    display: flex; align-items: center; justify-content: flex-end; gap: 6px;
    font-weight: 500; font-size: 12.5px; color: var(--ink);
  }
</style>
</head>
<body>
<div class="flyer">
  <svg class="art" width="764" height="1080" viewBox="0 0 764 1080">
    <defs>
      <linearGradient id="wallTone" x1="0" y1="0" x2="1" y2="1">
        <stop offset="0" stop-color="#8c8c8c"/><stop offset="1" stop-color="#5e5e5e"/>
      </linearGradient>
      <linearGradient id="sunsetTone" x1="0" y1="0" x2="0" y2="1">
        <stop offset="0" stop-color="#7d9cc4"/><stop offset="0.55" stop-color="#d9a46a"/><stop offset="1" stop-color="#b4561f"/>
      </linearGradient>
      <linearGradient id="workTone" x1="0" y1="0" x2="1" y2="1">
        <stop offset="0" stop-color="#dedede"/><stop offset="1" stop-color="#9a9a9a"/>
      </linearGradient>
      <linearGradient id="duoTone" x1="0" y1="0" x2="1" y2="1">
        <stop offset="0" stop-color="#1459ad"/><stop offset="1" stop-color="#0a3674"/>
      </linearGradient>
    </defs>

    <polygon class="corner-accent" points="311,0 764,0 764,393" fill="var(--orange)"/>

    <polygon points="565,14 753,118 753,329 565,433 389,329 389,118" fill="#fff"/>
    <polygon role="img" aria-label="Photo of a hand pressing a wall light switch"
      points="565,24 745,123 745,324 565,424 397,324 397,123" fill="url(#wallTone)"/>

    <polygon points="630,306 727,362 727,478 630,534 531,478 531,362" fill="#fff"/>
    <polygon class="quote-badge" points="630,316 718,368 718,471 630,523 540,471 540,368" fill="var(--blue)"/>
    <polygon points="630,326 709,373 709,466 630,513 549,466 549,373" fill="none" stroke="#fff" stroke-width="1.2"/>

    <polygon role="img" aria-label="Blue toned photo of an electrician working on a switchboard"
      points="0,682 460,1080 0,1080" fill="url(#duoTone)"/>
    <polygon points="154,586 289,658 289,822 154,894 20,822 20,658" fill="#fff"/>
    <polygon role="img" aria-label="Photo of power transmission towers at sunset"
      points="154,594 281,662 281,818 154,886 28,818 28,662" fill="url(#sunsetTone)"/>
    <polygon points="292,826 390,880 390,1000 292,1050 195,1000 195,880" fill="#fff"/>
    <polygon role="img" aria-label="Photo of an electrician on a ladder fitting a ceiling"
      points="292,834 382,884 382,996 292,1042 203,996 203,884" fill="url(#workTone)"/>

    <polygon class="services-tab" points="324,593 548,593 568,633 324,633" fill="var(--blue)"/>
    <polygon points="553,599 563,599 584,635 574,635" fill="#555"/>
    <line x1="580" y1="634" x2="718" y2="634" stroke="#555" stroke-width="2"/>

    <g stroke="#555" stroke-width="1.4" stroke-dasharray="1.5 2.5" fill="none">
      <line x1="324" y1="732" x2="722" y2="732"/>
      <line x1="324" y1="825" x2="722" y2="825"/>
      <line x1="520" y1="650" x2="520" y2="815"/>
    </g>

    <g class="icon-house" fill="none" stroke-width="2" stroke-linejoin="round">
      <polyline points="395,682 417,659 439,682" stroke="var(--blue)"/>
      <polyline points="400,678 400,692 434,692 434,678" stroke="var(--orange)"/>
      <rect x="413" y="681" width="8" height="11" stroke="var(--blue)"/>
    </g>
    <g class="icon-buildings" fill="none" stroke-width="2">
      <rect x="601" y="654" width="20" height="38" stroke="var(--blue)"/>
      <rect x="621" y="670" width="16" height="22" stroke="var(--blue)"/>
      <rect x="600" y="673" width="8" height="19" stroke="var(--orange)"/>
      <g fill="var(--orange)" stroke="none">
        <rect x="607" y="660" width="3" height="3"/><rect x="613" y="660" width="3" height="3"/>
        <rect x="625" y="676" width="3" height="3"/><rect x="630" y="676" width="3" height="3"/>
        <rect x="625" y="683" width="3" height="3"/><rect x="630" y="683" width="3" height="3"/>
      </g>
    </g>
    <g class="icon-factory" fill="none" stroke-width="2" stroke-linejoin="round">
      <polyline points="398,780 398,765 410,759 410,765 422,759 422,765 434,759 438,759 438,747 442,747 442,780 398,780" stroke="var(--blue)"/>
      <rect x="432" y="744" width="3" height="15" stroke="var(--orange)"/>
      <line x1="404" y1="774" x2="432" y2="774" stroke="var(--orange)" stroke-dasharray="3 2"/>
    </g>
    <g class="icon-crane" fill="none" stroke-width="2">
      <line x1="614" y1="752" x2="614" y2="782" stroke="var(--blue)"/>
      <line x1="596" y1="752" x2="636" y2="752" stroke="var(--blue)"/>
      <line x1="606" y1="782" x2="622" y2="782" stroke="var(--blue)"/>
      <rect x="630" y="749" width="7" height="7" stroke="var(--blue)"/>
      <rect x="594" y="764" width="10" height="18" stroke="var(--orange)"/>
      <line x1="600" y1="752" x2="600" y2="762" stroke="var(--orange)"/>
    </g>

    <g class="icon-phone" fill="none" stroke="var(--orange)" stroke-width="2">
      <path d="M450,943 c2,-4 6,-6 8,-4 l3,5 c1,2 -1,3 -3,4 c1,4 4,7 8,9 c1,-2 2,-4 4,-3 l5,3 c2,2 0,6 -4,8 c-10,2 -24,-12 -21,-22 z"/>
      <path d="M466,936 a10,10 0 0 1 10,10"/>
      <path d="M466,930 a16,16 0 0 1 16,16"/>
    </g>
    <g class="icon-mail" fill="none" stroke="var(--blue)" stroke-width="1.4">
      <rect x="445" y="1024" width="14" height="11"/>
      <polyline points="445,1024 452,1031 459,1024"/>
    </g>
  </svg>

  <div class="brand-mark"></div>
  <div class="brand-name">BRENMORE ELECTRICAL</div>
  <div class="brand-tagline">POWERING YOUR PROJECTS</div>

  <div class="intro">
    <p>At Brenmore Electrical, our team of experienced and qualified electricians are dedicated to providing top-quality electrical services to residential, commercial, construction, and industrial clients throughout the Sydney area. We offer a comprehensive range of services including installations, repairs, and maintenance of electrical systems.</p>
    <p>Our company is founded on the principle of delivering reliable, affordable, and efficient electrical solutions to our customers. We use cutting-edge technology and high-quality materials to ensure the safety, efficiency, and excellence of every project we undertake.</p>
    <p>At Brenmore Electrical, we believe that customer satisfaction is the key to our success. That's why we always strive to exceed your expectations and provide you with the best possible service.</p>
  </div>

  <div class="quote-label">GET A<br>FREE<br>QUOTE</div>

  <div class="services-title">OUR SERVICES</div>
  <div class="service" style="left:322px;top:696px;"><svg class="bolt" viewBox="0 0 12 20"><polygon points="8,0 1,12 6,12 3,20 11,7 6,7" fill="var(--yellow)"/></svg>Residential</div>
  <div class="service" style="left:522px;top:696px;"><svg class="bolt" viewBox="0 0 12 20"><polygon points="8,0 1,12 6,12 3,20 11,7 6,7" fill="var(--yellow)"/></svg>Commercial</div>
  <div class="service" style="left:322px;top:786px;"><svg class="bolt" viewBox="0 0 12 20"><polygon points="8,0 1,12 6,12 3,20 11,7 6,7" fill="var(--yellow)"/></svg>Industrial</div>
  <div class="service" style="left:522px;top:786px;"><svg class="bolt" viewBox="0 0 12 20"><polygon points="8,0 1,12 6,12 3,20 11,7 6,7" fill="var(--yellow)"/></svg>Construction</div>

  <div class="contact-note"><span class="lead">So, contact us today to schedule an appointment</span><br>with our experienced and licensed electricians<br>for your next electrical project</div>
  <div class="phone">+0400 555 218</div>
  <div class="website">brenmoreelectrical-example.com</div>
  <div class="email">office@brenmoreelectrical-example.com</div>
</div>
</body>
</html>
```